K7 Dynamics Stationery Design Project

We are looking to have stationary designs created for our company branding materials. We are looking for the following to be created.
1. Business Cards (front & back)
2. Letterhead
3. Envelopes #10
We are a new web design, development and marketing firm. Primary color scheme is desired to be blue/grey/white. This web start-up is owned and operated by individuals with 15+ years experience each in the industry so should not look as though it is a start-up by young/inexperienced individuals.
We build website & custom applications/software. In addition we provide the full spectrum of web marketing solutions including SEO, PPC, Social Media, Branding, Content Marketing and PR.
Please let us know if you have any questions. Looking forward to seeing all the amazing design ideas.
Attached is our logo.
Thanks!
Target Market(s)
Company will be nearly 100% business to business sales. Looking to work with companies that are already established, with a website, who want to take their website and/or online marketing efforts to the next level.
Industry/Entity Type
Marketing
Look and feel

```html
<!DOCTYPE html>
<html lang="en">
<head>
<meta charset="utf-8">
<title>K7 Dynamics – Business Card</title>
<link rel="stylesheet" href="https://fonts.googleapis.com/css2?family=Jost:wght@400;500;600;700&display=swap">
<style>
  :root {
    --bg: #e9ecef;
    --blue-light: #22b6e6;
    --blue: #1793d6;
    --blue-deep: #1a6bcc;
    --navy: #1f2a44;
    --ink: #2a2d33;
    --white: #ffffff;
    --card-shadow: 0 10px 30px rgba(20, 30, 50, 0.18);
  }
  * { box-sizing: border-box; margin: 0; padding: 0; }
  html, body {
    width: 1200px;
    height: 900px;
    overflow: hidden;
    background: var(--bg);
    font-family: "Jost", "Futura", sans-serif;
  }
  .canvas { position: relative; width: 1200px; height: 900px; }

  .card {
    position: absolute;
    width: 560px;
    height: 320px;
    overflow: hidden;
    box-shadow: var(--card-shadow);
  }

  /* Back of card */
  .card--back { left: 80px; top: 110px; }
  .card--back .pattern-field {
    position: absolute; inset: 0;
    background: linear-gradient(160deg, var(--blue-light) 0%, var(--blue) 50%, var(--blue-deep) 100%);
  }
  .card--back .brand {
    position: absolute; left: 0; right: 0; top: 110px;
    text-align: center; color: var(--white);
  }
  .brand__name {
    display: inline-flex; align-items: center; gap: 10px;
    font-weight: 700; font-size: 34px; letter-spacing: 1px; line-height: 1;
    white-space: nowrap;
  }
  .brand__dot { width: 18px; height: 18px; border-radius: 50%; background: currentColor; flex: none; }
  .brand__tagline { font-size: 13px; font-weight: 500; margin-top: 6px; white-space: nowrap; }
  .card--back .brand__url { font-size: 17px; font-weight: 700; margin-top: 26px; }

  /* Front of card */
  .card--front { left: 560px; top: 470px; background: var(--white); }
  .front__side-bar {
    position: absolute; left: 0; top: 120px; width: 36px; height: 118px;
    background: var(--blue);
  }
  .front__band {
    position: absolute; left: 290px; right: 0; top: 96px; height: 122px;
    background: linear-gradient(90deg, var(--blue) 0%, var(--blue-light) 100%);
  }
  .front__brand {
    position: absolute; left: 52px; top: 160px; color: var(--navy);
  }
  .front__brand .brand__name { font-size: 21px; gap: 8px; letter-spacing: 0.5px; }
  .front__brand .brand__dot { width: 12px; height: 12px; background: var(--blue); }
  .front__brand .brand__tagline { font-size: 9.5px; margin-top: 4px; }

  .holder {
    position: absolute; left: 302px; top: 64px;
    color: var(--ink); font-size: 19px; font-weight: 600; white-space: nowrap;
  }
  .holder__role { font-size: 12px; font-weight: 500; }
  .contact {
    position: absolute; left: 302px; top: 110px;
    color: var(--white); font-size: 13px; line-height: 1.3; white-space: nowrap;
  }
  .contact__address { margin-bottom: 14px; }
  .contact__label { color: var(--navy); margin-right: 4px; }
  .front__url {
    position: absolute; left: 330px; top: 236px;
    color: var(--ink); font-size: 16px; font-weight: 600;
  }
</style>
</head>
<body>
<main class="canvas">

  <section class="card card--back">
    <div class="pattern-field" role="img" aria-label="Blue gradient with a repeating brand pattern"></div>
    <div class="brand">
      <div class="brand__name"><span class="brand__dot"></span>K7 DYNAMICS</div>
      <div class="brand__tagline">Web Design, Development and Marketing</div>
      <div class="brand__url">www.k7dynamics.com</div>
    </div>
  </section>

  <section class="card card--front">
    <div class="front__side-bar"></div>
    <div class="front__band"></div>

    <div class="front__brand">
      <div class="brand__name"><span class="brand__dot"></span>K7 DYNAMICS</div>
      <div class="brand__tagline">Web Design, Development and Marketing</div>
    </div>

    <div class="holder">Marcus Hale <span class="holder__role">Manager</span></div>

    <div class="contact">
      <p class="contact__address">0 Harbor Line Road, Suite 00000,<br>Ashford, NC 00000</p>
      <p><span class="contact__label">P:</span>+1 000 000 0011</p>
      <p><span class="contact__label">F:</span>+1 000 000 0011</p>
      <p><span class="contact__label">E:</span>marcus@k7dynamics.com</p>
    </div>

    <div class="front__url">www.k7dynamics.com</div>
  </section>

</main>
</body>
</html>
```